Business Cards + Flyer + Letterhead for Care Recruitment Agency

We are a recruitment agency for the health & care sector. We need designs made for business cards, A5 double-sided flyer, and a letterhead template.

Our branding message is professionalism, care, compassion, expertise. We are experts in recruitment for the care & health industry.

Our logo source files and colours are here - https://www.fileporta.net/sh/qrvn82lopx4kdte/BBBgKy8LMQ27uTnPwZxHcVobsa?dl=0

For the business card, I have attached an example we like. We want a vertical business card design, something very similar to the example given. The design should match our logo in terms of brand colors. On one side should be our logo, our website (www.hollowmere.co.uk) and Care Recruitment Specialists written somewhere visible that fits, between our logo and the website at the bottom. On the other side should be our details.

Details on the front:

Logo with slogan
Care Recruitment Specialists
www.hollowmere.co.uk

Details on the back:

Tobias Orlund
Managing Director

Pellam House, 31-39 Larkfield St, Birmingham, B4 7QD
07612 495371
tobias@hollowmere.co.uk
www.hollowmere.co.uk

Marnie Holloway
Business Development Director

07831 204968
marnie@hollowmere.co.uk
www.hollowmere.co.uk

For the A5 flyer, I have attached some pictures we've used for the website, which could be used for the flyer as well. To get a better idea of our branding, please visit our website - https://hollowmere.co.uk/

The text for the flyer is also attached.

Finally, the letterhead template should be a docx template with our logo and our identifiable branding (the same shapes and matching colours you will come up with for the business cards and flyer).

```html
<!DOCTYPE html>
<html lang="en">
<head>
<meta charset="utf-8">
<title>Hollowmere Letterhead</title>
<link href="https://fonts.googleapis.com/css2?family=Montserrat:wght@300;400;700&family=Encode+Sans+Semi+Condensed:wght@300&family=Mulish:wght@400&display=swap" rel="stylesheet">
<style>
  :root {
    --backdrop: #dcdcdc;
    --paper: #ffffff;
    --navy: #1f2d6b;
    --brand-blue: #2a8fd6;
    --ink: #555657;
    --ink-dark: #4a4b4d;
  }
  * { margin: 0; padding: 0; box-sizing: border-box; }
  html, body {
    width: 1056px; height: 1200px; overflow: hidden;
    background: var(--backdrop);
  }
  .letterhead {
    position: absolute; left: 104px; top: 0;
    width: 848px; height: 1200px;
    background: var(--paper);
  }
  .brand {
    position: absolute; left: 0; top: 64px; width: 100%;
    text-align: center;
  }
  .brand-mark {
    display: block; width: 84px; height: 84px; margin: 0 auto 14px;
    border-radius: 50%; background: var(--brand-blue);
  }
  .brand-name {
    font-family: "Montserrat", sans-serif; font-weight: 700;
    font-size: 23px; letter-spacing: 2.6px; color: var(--navy);
    line-height: 1;
  }
  .brand-tagline {
    margin-top: 6px;
    font-family: "Montserrat", sans-serif; font-weight: 400;
    font-size: 10.5px; letter-spacing: 2.2px; color: var(--brand-blue);
    text-transform: uppercase;
  }
  .recipient {
    position: absolute; left: 80px; top: 328px;
    font-family: "Montserrat", sans-serif; color: var(--ink);
  }
  .letter-date { font-weight: 300; font-size: 18.5px; line-height: 24px; }
  .recipient-name {
    font-weight: 700; font-size: 30px; line-height: 36px;
    margin-top: 8px; color: var(--ink-dark); text-transform: uppercase;
  }
  .recipient-title { font-weight: 300; font-size: 18.5px; line-height: 24px; margin-top: 4px; }
  .letter-body {
    position: absolute; left: 80px; top: 478px; width: 688px;
    font-family: "Encode Sans Semi Condensed", sans-serif; font-weight: 300;
    font-size: 16px; line-height: 29.5px; color: var(--ink);
    text-align: justify;
  }
  .letter-body p { margin-bottom: 29.5px; }
  .sign-off {
    position: absolute; left: 80px; top: 929px;
    font-family: "Encode Sans Semi Condensed", sans-serif; font-weight: 300;
    font-size: 18.5px; color: var(--ink);
  }
  .signature {
    position: absolute; left: 83px; top: 976px;
    width: 88px; height: 61px; border-radius: 6px;
    background: linear-gradient(135deg, #e6e9f2, #d3d8e8);
  }
  .contact {
    position: absolute; left: 0; top: 1110px; width: 100%;
    text-align: center; font-family: "Mulish", sans-serif;
    font-size: 13.5px; color: var(--navy);
  }
  .contact-address { line-height: 22px; }
  .contact-lines {
    margin-top: 3px; display: flex; justify-content: center; align-items: center; gap: 12px;
  }
  .contact-item { display: inline-flex; align-items: center; gap: 12px; }
  .contact-item svg { width: 13px; height: 13px; fill: none; stroke: var(--brand-blue); stroke-width: 1.6; }
</style>
</head>
<body>
  <main class="letterhead">
    <header class="brand">
      <span class="brand-mark"></span>
      <div class="brand-name">HOLLOWMERE</div>
      <div class="brand-tagline">Care recruitment specialists</div>
    </header>

    <section class="recipient">
      <div class="letter-date">10 December, 2020</div>
      <div class="recipient-name">Daniel Rowe</div>
      <div class="recipient-title">Cheif Executive Officer</div>
    </section>

    <section class="letter-body">
      <p>Contrary to popular belief, Lorem Ipsum is not simply random text. It has roots in a piece of classical Latin literature from 45 BC, making it over 2000 years old. Edwin Marlowe, a Latin professor at Ashbury College in Virginia, looked up one of the more obscure Latin words, consectetur.</p>
      <p>Lorem Ipsum comes from sections 1.10.32 and 1.10.33 of "de Finibus Bonorum et Malorum" (The Extremes of Good and Evil) by Aurelian Tessius, written in 45 BC. This book is a treatise on the theory of ethics, very popular during the Renaissance. The first line of Lorem Ipsum.</p>
      <p>The standard chunk of Lorem Ipsum used since the 1500s is reproduced below for those interested. Sections 1.10.32 and 1.10.33 from "de Finibus Bonorum et Malorum" by Aurelian Tessius are also reproduced in their exact original.</p>
      <p>The standard chunk of Lorem Ipsum used since the 1500s is reproduced below for those interested.</p>
    </section>

    <div class="sign-off">Best Regards</div>
    <div class="signature" role="img" aria-label="Handwritten signature of the sender"></div>

    <footer class="contact">
      <div class="contact-address">Pellam House, 31-39 Larkfield St, Birmingham, B4 7QD</div>
      <div class="contact-lines">
        <span class="contact-item">
          <svg viewBox="0 0 16 16" aria-hidden="true"><path d="M3 2l3 1 1 3-2 1.5a8 8 0 0 0 3.5 3.5L10 9l3 1 1 3-2 1.5C7 14 2 9 1.5 4z"/></svg>
          07612 495371
        </span>
        <span class="contact-item">
          <svg viewBox="0 0 16 16" aria-hidden="true"><rect x="1.5" y="3.5" width="13" height="9"/><path d="M1.5 3.5l6.5 5 6.5-5"/></svg>
          tobias@hollowmere.co.uk
        </span>
        <span class="contact-item">
          <svg viewBox="0 0 16 16" aria-hidden="true"><circle cx="8" cy="8" r="6.5"/><path d="M1.5 8h13M8 1.5c-3 3-3 10 0 13M8 1.5c3 3 3 10 0 13"/></svg>
          www.hollowmere.co.uk
        </span>
      </div>
    </footer>
  </main>
</body>
</html>
```